Business Card Design Project

We need a business card for a chiropractic and rehabilitation center. We already have a logo and need the card to follow the color and feel of the logo.

Target Market(s)

adults 30-55 that have some ache or pain that is interfering with their life, so much as they are ready to do something about it.

Industry/Entity Type

Business

```html
<!DOCTYPE html>
<html lang="en">
<head>
<meta charset="utf-8">
<title>Vitalcore Wellness – Business Card</title>
<link rel="stylesheet" href="https://fonts.googleapis.com/css2?family=Arimo:wght@400;700&family=Jura:wght@500;600&display=swap">
<style>
  :root {
    --canvas: #eeeeee;
    --card: #ffffff;
    --orange: #f5922a;
    --gray-dark: #58585a;
    --gray-mid: #8a8a8c;
    --red: #c1272d;
    --ink: #111111;
    --white: #ffffff;
  }
  html, body {
    margin: 0;
    padding: 0;
    width: 1080px;
    height: 1200px;
    overflow: hidden;
    background: var(--canvas);
  }
  .business-card {
    position: absolute;
    left: 40px;
    top: 308px;
    width: 1000px;
    height: 584px;
    background: var(--card);
    box-shadow: 0 6px 18px rgba(0,0,0,0.12);
  }
  .business-card svg { display: block; }
  .brand-name { font-family: "Arimo", sans-serif; font-weight: 700; fill: var(--gray-dark); letter-spacing: 1px; }
  .person-name { font-family: "Jura", sans-serif; font-weight: 600; fill: var(--red); }
  .person-title { font-family: "Arimo", sans-serif; font-weight: 400; fill: var(--gray-dark); }
  .address { font-family: "Arimo", sans-serif; font-weight: 400; fill: var(--ink); white-space: pre; }
  .contact-label, .contact-value { font-family: "Arimo", sans-serif; font-weight: 400; fill: var(--white); }
</style>
</head>
<body>
<div class="business-card">
  <svg width="1000" height="584" viewBox="0 0 1000 584" xmlns="http://www.w3.org/2000/svg">
    <defs>
      <linearGradient id="swoosh-gray" x1="0" y1="0" x2="0" y2="1">
        <stop offset="0" stop-color="#ffffff"/>
        <stop offset="0.35" stop-color="#8a8a8c"/>
        <stop offset="1" stop-color="#58585a"/>
      </linearGradient>
      <linearGradient id="rule-fade-right" x1="0" y1="0" x2="1" y2="0">
        <stop offset="0" stop-color="#58585a"/>
        <stop offset="1" stop-color="#ffffff"/>
      </linearGradient>
      <linearGradient id="rule-fade-left" x1="0" y1="0" x2="1" y2="0">
        <stop offset="0" stop-color="#ffffff"/>
        <stop offset="1" stop-color="#58585a"/>
      </linearGradient>
      <linearGradient id="corner-arc" x1="0" y1="0" x2="0" y2="1">
        <stop offset="0" stop-color="#f5922a"/>
        <stop offset="1" stop-color="#ffffff"/>
      </linearGradient>
    </defs>

    <!-- corner accent -->
    <path class="corner-block" d="M0 0 H106 C70 26 50 70 48 124 H0 Z" fill="var(--gray-dark)"/>
    <path class="corner-arc" d="M112 0 C76 26 56 72 56 130" fill="none" stroke="url(#corner-arc)" stroke-width="6"/>

    <!-- brand -->
    <text class="brand-name" x="127" y="198" font-size="40">VITALCORE WELLNESS</text>

    <!-- contact panel -->
    <path class="panel-swoosh" d="M622 160 C692 262 694 432 540 584 L576 584 C704 452 708 280 652 163 Z" fill="url(#swoosh-gray)"/>
    <path class="contact-panel" d="M652 163 H1000 V584 H576 C704 452 708 280 652 163 Z" fill="var(--orange)"/>

    <g class="contact-list">
      <text class="contact-label" x="697" y="242" font-size="25">Phone:</text>
      <text class="contact-value" x="697" y="274" font-size="25">555.0142.730</text>
      <text class="contact-label" x="697" y="322" font-size="25">Fax:</text>
      <text class="contact-value" x="697" y="355" font-size="25">555.0142.731</text>
      <text class="contact-label" x="697" y="403" font-size="25">Email:</text>
      <text class="contact-value" x="698" y="437" font-size="20">info@vitalcorewellness.com</text>
      <text class="contact-label" x="697" y="481" font-size="25">Website:</text>
      <text class="contact-value" x="698" y="516" font-size="20">www.vitalcorewellness.com</text>
    </g>

    <!-- name block -->
    <rect class="name-rule-top" x="0" y="317" width="456" height="7" fill="url(#rule-fade-right)"/>
    <text class="person-name" x="440" y="382" font-size="46" text-anchor="end">Marisol Vantreece</text>
    <text class="person-title" x="439" y="418" font-size="26" text-anchor="end">Managing Director</text>
    <rect class="name-rule-bottom" x="0" y="436" width="458" height="8" fill="url(#rule-fade-left)"/>

    <!-- address -->
    <text class="address" x="49" y="534" font-size="26">220 Mill Road, Suite 4,  Ashford, NJ 08500</text>
  </svg>
</div>
</body>
</html>
```